IV Nutritional Clinic Web Design

We are working with Velmo. They are an IV Nutritional Clinic and in need of a new website design.
Some sites to use for inspiration:
https://brantlowcare.example
https://www.zolvarihealth.example
https://www.quellspa.example
https://pimrolift.example
https://www.dorvak-well.example/pages/iv-therapy-west-hollywood
https://www.tqoncowell.example/cancer-care/iv-drips/
https://drelmavita.example
https://salbrikmed.example
Thank you for taking the time to consider designing a website for us. We are web developers based in Stockton, CA, USA. Most of our projects go through the same process. Understanding this process may help you win a project with us. We custom-code all of our websites in-house. We don’t have any requirements as to what tools you use for your design, but we prefer Figma files. For any design that we label as four-stars, we send it to the client for review. The client picks the final design they want us to use. Once we complete this process, we will continue to show additional clients all the four-star sites and purchase them later. Your designs will have multiple chances to sell. For better chances of success, we ask that you follow these guidelines.
IMAGES:
If you use any images or icons in the design, we ask that you have a link to the asset so we can purchase the image/icon. Most of the designs we submit do not have the customer’s images on them unless they have some great images. Be creative; show us the feeling you are trying to portray with your image choices. Use any royalty-free site you choose. We subscribe to Corvix and mainly use their images, but we can purchase images outside of Corvix.
PLEASE NOTE: we will not submit designs to clients with watermarks on the images.
FONTS:
We ask that you identify the fonts used in the design. This can be done in a message if you want. We typically use Lumen Typeset and Corvix Fonts.
CONTENT:
We're always open to different content and ideas. We often submit designs with stock images so the client can see our vision. We typically take pictures after the website launch to use their images with our vision. Lorem Ipsum is fine for paragraphs, but we ask that you write the headers in correct English. We want to be able to show the vision and identify the sections of the website.
INSPIRATION:
We typically add a couple of links in the brief of websites we like to help you get started in your design.
REVISIONS:
We do not often ask for revisions of the designs unless we see something in the design that may not appeal to the client. If there are slight changes that we want to make, we do that in the development process.
FEEDBACK:
We rarely give feedback on designs during the design process. We are working on many website projects and do not have the time to provide feedback. We usually respond if your request is well thought out and asks specific questions, but a note asking “feedback, please” usually goes unanswered.
Number of Pages Required
1 page
Look and feel
Each slider illustrates characteristics of the customer's brand and the style your logo design should communicate.

```html
<!DOCTYPE html>
<html lang="en">
<head>
<meta charset="utf-8">
<title>Velmo Hydration – IV Therapy</title>
<link href="https://fonts.googleapis.com/css2?family=Montserrat:wght@400;500;600;700;800&display=swap" rel="stylesheet">
<style>
:root{
  --navy:#28267f;
  --green:#6b9a38;
  --green-dark:#5b8a2c;
  --mint:#eef6df;
  --lav:#eff0fa;
  --text:#3c3c4a;
  --muted:#5d5d6b;
  --white:#ffffff;
  --line:#d9dbe8;
}
*{box-sizing:border-box;margin:0;padding:0}
html,body{width:1200px;height:4511px;overflow:hidden}
body{font-family:'Montserrat',sans-serif;color:var(--text);background:var(--white);position:relative}
.abs{position:absolute}
a{color:inherit;text-decoration:none}
.btn{position:absolute;display:flex;align-items:center;justify-content:center;border-radius:30px;color:#fff;font-weight:700;font-size:14px;letter-spacing:.2px}
.btn-navy{background:var(--navy)}
.btn-green{background:var(--green)}
.accent{color:var(--green)}

/* header */
.site-header{position:absolute;left:0;top:0;width:1200px;height:82px;background:var(--mint)}
.brand{position:absolute;left:112px;top:8px;font-size:50px;font-weight:800;color:var(--navy);letter-spacing:1px}
.main-nav{position:absolute;top:34px;left:366px;font-size:12px;font-weight:500;color:var(--navy)}
.main-nav a{position:absolute;white-space:nowrap}
.main-nav .active{font-weight:700}

/* hero */
.hero{position:absolute;left:0;top:82px;width:1200px;height:558px;background:linear-gradient(90deg,#eef6df 0%,#e8f2d6 38%,#cfd9c9 55%,#e4e7e3 75%,#c9d0c8 100%)}
.hero-badge{position:absolute;left:112px;top:170px;height:38px;display:flex;font-weight:700;font-size:20px;color:#fff}
.hero-badge span{display:flex;align-items:center;padding:0 12px}
.hero-badge .b1{background:var(--navy)}
.hero-badge .b2{background:var(--green);padding:0 20px}
.hero-title{position:absolute;left:112px;top:222px;font-size:40px;line-height:50px;font-weight:700;color:#1d1d2b}
.hero-title .l1{color:var(--navy)}

/* about */
.about-frame{position:absolute;left:119px;top:722px;width:166px;height:122px;border:2px solid var(--green);border-radius:6px 0 0 6px}
.about-block{position:absolute;left:420px;top:1025px;width:158px;height:117px;background:var(--navy);border-radius:4px}
.about-photo{position:absolute;left:147px;top:741px;width:407px;height:368px;background:linear-gradient(135deg,#5fa6c7,#d8e2e8 45%,#f2efec 70%,#b9c9d3)}
.section-title{font-size:40px;font-weight:700;color:var(--navy)}
.about-title{position:absolute;left:615px;top:742px}
.about-text{position:absolute;left:620px;top:808px;width:420px;font-size:14.5px;line-height:28.3px;color:var(--text)}

/* services */
.services{position:absolute;left:0;top:1244px;width:1200px;height:534px;background:radial-gradient(ellipse at 50% 55%,#e9f3d8 0%,#d7e9bb 45%,#bcd99a 100%)}
.services-title{position:absolute;left:0;top:60px;width:1200px;text-align:center}
.svc-card{position:absolute;top:147px;width:226px;height:291px;background:#fff;border-radius:4px;text-align:center}
.svc-icon{position:absolute;left:72px;top:22px;width:82px;height:82px;border-radius:50%;border:2px dashed var(--green);display:flex;align-items:center;justify-content:center}
.svc-icon i{width:68px;height:68px;border-radius:50%;background:var(--navy);display:flex;align-items:center;justify-content:center}
.svc-name{position:absolute;left:0;top:128px;width:226px;font-size:16.5px;font-weight:600;color:#1d1d2b;line-height:28px}
.svc-desc{position:absolute;left:18px;width:190px;font-size:13.5px;line-height:25.5px;color:var(--muted)}
.svc-link{position:absolute;left:46px;bottom:22px;font-size:13.5px;font-weight:700;color:var(--green);display:flex;align-items:center;gap:8px}
.svc-card.active{border-bottom:5px solid var(--navy)}
.svc-arrow{position:absolute;top:292px;width:36px;height:36px;border-radius:50%;display:flex;align-items:center;justify-content:center}

/* iv band */
.iv-band{position:absolute;left:0;top:1778px;width:1200px;height:491px;background:linear-gradient(100deg,#5f8f22 0%,#a5c43b 35%,#e7c56a 60%,#f3a93a 80%,#e9cf82 100%)}
.iv-circle{position:absolute;left:102px;top:1817px;width:396px;height:396px;border-radius:50%;background:var(--green);text-align:center;color:#fff}
.iv-circle h2{position:absolute;top:48px;left:0;width:396px;font-size:29px;line-height:41px;font-weight:600}
.iv-circle p{position:absolute;top:136px;left:40px;width:316px;font-size:14px;line-height:28.3px}

/* how it works */
.how-title{position:absolute;left:0;top:2338px;width:1200px;text-align:center}
.step-ring{position:absolute;width:124px;height:124px;border-radius:50%;background:#fff;box-shadow:0 0 0 2px #d7d9ec,0 6px 16px rgba(40,38,127,.12);display:flex;align-items:center;justify-content:center}
.step-ring i{width:104px;height:104px;border-radius:50%;border:2px solid var(--navy);display:flex;align-items:center;justify-content:center}
.step{position:absolute;width:240px;text-align:center}
.step h3{font-size:20px;font-weight:700;color:#1d1d2b;line-height:29px}
.step p{font-size:14px;line-height:29px;color:var(--muted);margin-top:10px}
.step a{display:block;font-size:16px;font-weight:700;color:var(--green);letter-spacing:.3px}

/* testimonials */
.reviews{position:absolute;left:0;top:2938px;width:1200px;height:592px;background:var(--lav)}
.reviews-title{position:absolute;left:112px;top:60px}
.rv-card{position:absolute;width:308px;height:300px;background:#fff;border-radius:4px}
.rv-card.focus{box-shadow:0 4px 18px rgba(40,38,127,.15)}
.rv-card p{position:absolute;left:24px;top:34px;width:262px;font-size:14px;line-height:28.5px;color:var(--muted)}
.rv-card hr{position:absolute;left:24px;top:170px;width:262px;border:0;border-top:2px solid var(--line)}
.rv-avatar{position:absolute;left:12px;top:184px;width:94px;height:94px;border-radius:50%;background:linear-gradient(160deg,#cfd6de,#8f9aa8)}
.rv-name{position:absolute;left:122px;top:196px;font-size:17px;font-weight:600;color:var(--navy)}
.rv-role{position:absolute;left:122px;top:226px;font-size:14px;color:var(--muted)}
.rv-stars{position:absolute;left:122px;top:250px;font-size:14px;color:#f2b21b;letter-spacing:1px}
.rv-mark{position:absolute;left:250px;top:220px;width:30px;height:30px;border-radius:50%;background:#e4e6f2}

/* contact */
.contact{position:absolute;left:0;top:3530px;width:1200px;height:596px;background:#232281}
.contact h2{position:absolute;left:0;top:70px;width:1200px;text-align:center;font-size:40px;font-weight:600;color:#fff}
.contact .lead{position:absolute;left:0;top:137px;width:1200px;text-align:center;font-size:14.5px;line-height:28px;color:#fff}
.field{position:absolute;height:49px;background:#fff;border-radius:25px;padding:0 22px;display:flex;align-items:center;justify-content:space-between;font-size:12.5px;color:#333;letter-spacing:.3px}
.field.msg{align-items:flex-start;padding-top:20px;border-radius:20px}

/* footer */
.site-footer{position:absolute;left:0;top:4126px;width:1200px;height:385px;background:#fff}
.foot-brand{position:absolute;left:112px;top:82px;font-size:52px;font-weight:800;color:var(--navy);letter-spacing:1px}
.foot-col{position:absolute;top:80px}
.foot-col h4{font-size:20px;font-weight:500;color:#1d1d2b;line-height:28px;letter-spacing:.3px}
.foot-col ul{list-style:none;margin-top:20px}
.foot-col li{font-size:14.5px;line-height:27.5px;color:#1d1d2b}
.contact-list li{display:flex;gap:6px;align-items:flex-start}
.news-note{font-size:12.5px;line-height:24px;color:var(--muted);margin-top:12px}
.news-input{margin-top:18px;width:216px;height:42px;border:1px solid var(--line);border-radius:4px;position:relative;font-size:12.5px;color:#444;display:flex;align-items:center;padding-left:10px}
.news-input b{position:absolute;right:-2px;top:-2px;width:48px;height:44px;background:var(--green);border-radius:4px;display:flex;align-items:center;justify-content:center}
.foot-rule{position:absolute;left:112px;top:315px;width:976px;border-top:1px solid #999}
.copyright{position:absolute;left:0;top:340px;width:1200px;text-align:center;font-size:13px;color:#333}
</style>
</head>
<body>

<header class="site-header">
  <div class="brand">VELMO</div>
  <nav class="main-nav">
    <a class="active" style="left:0">HOME</a>
    <a style="left:72px">ABOUT US</a>
    <a style="left:168px">SERVICES</a>
    <a style="left:259px">TESTIMONIALS</a>
    <a style="left:384px">CONTACT</a>
  </nav>
  <a class="btn btn-navy" style="left:839px;top:19px;width:251px;height:46px;font-size:14px">BOOK AN APPOINTMENT</a>
</header>

<section class="hero" role="img" aria-label="Client relaxing in a white robe while a nurse sets up an IV drip">
</section>
<div class="hero-badge"><span class="b1">VELMO</span><span class="b2">HYDRATION</span></div>
<h1 class="hero-title"><span class="l1">Revitalize Your Body,</span><br>Reclaim Your Energy –<br><span class="accent">IV Therapy</span> for Optimal<br>Wellness.</h1>
<a class="btn btn-navy" style="left:114px;top:447px;width:158px;height:47px">BOOK NOW</a>

<!-- about -->
<div class="about-frame"></div>
<div class="about-block"></div>
<div class="about-photo" role="img" aria-label="Woman holding a phone while receiving IV therapy in a treatment chair"></div>
<h2 class="section-title about-title">About <span class="accent">Us</span></h2>
<p class="about-text">Lorem Ipsum is simply dummy text of the printing and typesetting industry. Lorem Ipsum has been the industry's standard dummy text ever since the 1500s, Lorem Ipsum has been the industry' Lorem Ipsum is simply dummy text of the printing and typesetting industry. Lorem Ipsum has been the industry's standard dummy text ever since the 1500s, Lorem Ipsum has been the industry'Lorem Ipsum is simply dummy text of the printing and typesetting</p>
<a class="btn btn-green" style="left:622px;top:1098px;width:158px;height:44px">READ MORE</a>

<!-- services -->
<section class="services" role="img" aria-label="Soft green background of vitamins and fresh produce">
  <h2 class="section-title services-title">Our <span class="accent">Services</span></h2>

  <div class="svc-arrow" style="left:50px;background:#9a9a9a"><svg width="14" height="14" viewBox="0 0 14 14"><path d="M9 2 4 7l5 5" fill="none" stroke="#fff" stroke-width="2"/></svg></div>
  <div class="svc-arrow" style="left:1110px;background:var(--green)"><svg width="14" height="14" viewBox="0 0 14 14"><path d="m5 2 5 5-5 5" fill="none" stroke="#fff" stroke-width="2"/></svg></div>

  <article class="svc-card" style="left:112px">
    <div class="svc-icon"><i><svg width="34" height="34" viewBox="0 0 34 34" fill="none" stroke="#fff" stroke-width="2"><rect x="10" y="5" width="12" height="18" rx="3"/><path d="M16 23v6M12 13h8"/></svg></i></div>
    <h3 class="svc-name">Hydration Therapy</h3>
    <p class="svc-desc" style="top:164px">Lorem Ipsum is simply dummy text of the printing and typesetting industry.</p>
    <a class="svc-link">READ MORE <svg width="18" height="12" viewBox="0 0 18 12"><path d="M0 6h16M11 1l5 5-5 5" fill="none" stroke="var(--navy)" stroke-width="2"/></svg></a>
  </article>
  <article class="svc-card active" style="left:362px">
    <div class="svc-icon"><i><svg width="34" height="34" viewBox="0 0 34 34" fill="none" stroke="#fff" stroke-width="2"><circle cx="17" cy="17" r="8"/><path d="M17 3v6M17 25v6M3 17h6M25 17h6"/></svg></i></div>
    <h3 class="svc-name">Immune Boost</h3>
    <p class="svc-desc" style="top:164px">Lorem Ipsum is simply dummy text of the printing and typesetting industry.</p>
    <a class="svc-link">READ MORE <svg width="18" height="12" viewBox="0 0 18 12"><path d="M0 6h16M11 1l5 5-5 5" fill="none" stroke="var(--navy)" stroke-width="2"/></svg></a>
  </article>
  <article class="svc-card" style="left:613px">
    <div class="svc-icon"><i><svg width="34" height="34" viewBox="0 0 34 34" fill="none" stroke="#fff" stroke-width="2"><path d="M19 3 9 19h8l-2 12 10-16h-8z"/></svg></i></div>
    <h3 class="svc-name">Energy Boost</h3>
    <p class="svc-desc" style="top:164px">Lorem Ipsum is simply dummy text of the printing and typesetting industry.</p>
    <a class="svc-link">READ MORE <svg width="18" height="12" viewBox="0 0 18 12"><path d="M0 6h16M11 1l5 5-5 5" fill="none" stroke="var(--navy)" stroke-width="2"/></svg></a>
  </article>
  <article class="svc-card" style="left:862px">
    <div class="svc-icon"><i><svg width="34" height="34" viewBox="0 0 34 34" fill="none" stroke="#fff" stroke-width="2"><path d="M17 4l3 9 9 3-9 3-3 9-3-9-9-3 9-3z"/></svg></i></div>
    <h3 class="svc-name">Beauty &amp; Skin<br>Health</h3>
    <p class="svc-desc" style="top:192px">Lorem Ipsum is simply dummy text of the printing</p>
    <a class="svc-link">READ MORE <svg width="18" height="12" viewBox="0 0 18 12"><path d="M0 6h16M11 1l5 5-5 5" fill="none" stroke="var(--navy)" stroke-width="2"/></svg></a>
  </article>
</section>

<!-- iv band -->
<section class="iv-band" role="img" aria-label="IV drip bag and tube against a bright green and orange background"></section>
<div class="iv-circle">
  <h2>What is IV<br>Nutritional Therapy?</h2>
  <p>Lorem Ipsum is simply dummy text of the printing and typesetting industry. Lorem Ipsum has been the industry's standard dummy text ever since the 1500s, Lorem Ipsum has been the industry'</p>
  <a class="btn btn-navy" style="left:119px;top:301px;width:158px;height:46px">READ MORE</a>
</div>

<!-- how it works -->
<h2 class="section-title how-title">How It <span class="accent">Works?</span></h2>
<svg class="abs" style="left:0;top:2400px" width="1200" height="240" viewBox="0 0 1200 240" fill="none" stroke="#444" stroke-width="1.5" stroke-dasharray="6 5">
  <path d="M104 32C150 30 175 50 190 70"/>
  <path d="M270 145C300 190 360 215 410 212"/>
  <path d="M515 180C570 140 610 120 650 100"/>
  <path d="M760 100C800 150 850 165 890 170"/>
  <path d="M1000 210C1050 205 1080 185 1100 175"/>
</svg>
<div class="step-ring" style="left:159px;top:2443px"><i><svg width="54" height="54" viewBox="0 0 54 54" fill="none" stroke="var(--navy)" stroke-width="2"><circle cx="17" cy="24" r="6"/><circle cx="37" cy="24" r="6"/><path d="M6 46c0-8 5-13 11-13s11 5 11 13M26 46c0-8 5-13 11-13s11 5 11 13"/><rect x="20" y="4" width="26" height="12" rx="2"/></svg></i></div>
<div class="step-ring" style="left:401px;top:2540px"><i><svg width="54" height="54" viewBox="0 0 54 54" fill="none" stroke="var(--navy)" stroke-width="2"><rect x="16" y="10" width="24" height="26" rx="3"/><path d="M28 17v12M22 23h12M6 44h18l12-6"/></svg></i></div>
<div class="step-ring" style="left:642px;top:2440px"><i><svg width="54" height="54" viewBox="0 0 54 54" fill="none" stroke="var(--green)" stroke-width="2"><circle cx="27" cy="23" r="13"/><circle cx="27" cy="23" r="5"/><path d="M18 36v12h18V36"/></svg></i></div>
<div class="step-ring" style="left:882px;top:2531px"><i><svg width="54" height="54" viewBox="0 0 54 54" fill="none" stroke="var(--green)" stroke-width="2"><circle cx="27" cy="10" r="5"/><path d="M12 8l9 12h12l9-12M21 20v12l-4 16M33 20v12l4 16"/><path d="M22 26l4 4 7-7"/></svg></i></div>

<div class="step" style="left:100px;top:2608px"><h3>Consultation</h3><p>Lorem Ipsum is simply dummy text of the printing and typesetting</p><a>READ MORE</a></div>
<div class="step" style="left:342px;top:2704px"><h3>Personalized<br>Treatment Plan</h3><p>Lorem Ipsum is simply dummy text</p><a>READ MORE</a></div>
<div class="step" style="left:584px;top:2604px"><h3>Relax &amp;<br>Rejuvenate</h3><p>Lorem Ipsum is simply dummy text</p><a>READ MORE</a></div>
<div class="step" style="left:824px;top:2701px"><h3>Feel the Results</h3><p>Lorem Ipsum is simply dummy text of the printing and typesetting</p><a>READ MORE</a></div>

<!-- testimonials -->
<section class="reviews">
  <h2 class="section-title reviews-title">What Our <span class="accent">Clients Say</span></h2>
  <div class="svc-arrow" style="left:995px;top:75px;background:#8b8b8b"><svg width="14" height="14" viewBox="0 0 14 14"><path d="M9 2 4 7l5 5" fill="none" stroke="#fff" stroke-width="2"/></svg></div>
  <div class="svc-arrow" style="left:1051px;top:75px;background:var(--green)"><svg width="14" height="14" viewBox="0 0 14 14"><path d="m5 2 5 5-5 5" fill="none" stroke="#fff" stroke-width="2"/></svg></div>

  <article class="rv-card" style="left:112px;top:147px">
    <p>Lorem Ipsum is simply dummy text of the printing and typesetting industry. Lorem Ipsum has been the industry's standard dummy text</p>
    <hr><div class="rv-avatar" role="img" aria-label="Portrait of client David"></div>
    <div class="rv-name">David</div><div class="rv-role">Client</div><div class="rv-stars">★★★★★</div><span class="rv-mark"></span>
  </article>
  <article class="rv-card focus" style="left:445px;top:198px">
    <p>Lorem Ipsum is simply dummy text of the printing and typesetting industry. Lorem Ipsum has been the industry's standard</p>
    <hr style="top:165px"><div class="rv-avatar" role="img" aria-label="Portrait of client Simon"></div>
    <div class="rv-name">Simon</div><div class="rv-role">Client</div><div class="rv-stars">★★★★★</div><span class="rv-mark"></span>
  </article>
  <article class="rv-card" style="left:780px;top:147px">
    <p>Lorem Ipsum is simply dummy text of the printing and typesetting industry. Lorem Ipsum has been the industry's standard dummy text</p>
    <hr><div class="rv-avatar" role="img" aria-label="Portrait of client Tom"></div>
    <div class="rv-name">Tom</div><div class="rv-role">Client</div><div class="rv-stars">★★★★★</div><span class="rv-mark"></span>
  </article>
  <article class="rv-card" style="left:1116px;top:198px">
    <p>Lorem Ipsum is simply dummy text of the printing and typesetting industry. Lorem Ipsum has been</p>
    <hr style="top:165px"><div class="rv-avatar" role="img" aria-label="Portrait of a client"></div>
  </article>
</section>

<!-- contact -->
<section class="contact">
  <h2>Contact Us</h2>
  <p class="lead">Lorem Ipsum is simply dummy text of the printing and typesetting industry.<br>Lorem Ipsum has been the industry's standard dummy text ever since the 1500s,</p>
  <div class="field" style="left:156px;top:210px;width:431px">NAME <svg width="18" height="18" viewBox="0 0 18 18" fill="none" stroke="#555" stroke-width="1.3"><circle cx="9" cy="6" r="4"/><path d="M2 17c0-4 3-6 7-6s7 2 7 6"/></svg></div>
  <div class="field" style="left:613px;top:210px;width:431px">CONTACT NUMBER <svg width="18" height="18" viewBox="0 0 18 18" fill="none" stroke="#555" stroke-width="1.3"><path d="M3 2h4l2 4-2 2c1 2 3 4 5 5l2-2 4 2v4c-8 0-15-7-15-15z"/></svg></div>
  <div class="field" style="left:156px;top:273px;width:431px">EMAIL ADDRESS <svg width="20" height="16" viewBox="0 0 20 16" fill="none" stroke="#555" stroke-width="1.3"><rect x="1" y="1" width="18" height="14"/><path d="m1 1 9 8 9-8"/></svg></div>
  <div class="field" style="left:613px;top:273px;width:431px">SUBJECT <svg width="14" height="18" viewBox="0 0 14 18" fill="none" stroke="#555" stroke-width="1.3"><rect x="1" y="1" width="12" height="16" rx="1"/><path d="M4 6h6M4 10h6"/></svg></div>
  <div class="field msg" style="left:156px;top:336px;width:888px;height:102px">YOUR MESSAGE <svg width="20" height="18" viewBox="0 0 20 18" fill="none" stroke="#555" stroke-width="1.3"><path d="M1 1h18v12H8l-4 4v-4H1z"/></svg></div>
  <a class="btn btn-green" style="left:513px;top:470px;width:179px;height:45px">SEND MESSAGE</a>
</section>

<!-- footer -->
<footer class="site-footer">
  <div class="foot-brand">VELMO</div>
  <div class="foot-col" style="left:371px">
    <h4>MAIN LINKS</h4>
    <ul><li>Home</li><li>About Us</li><li>Services</li><li>Testimonials</li><li>Contact</li></ul>
  </div>
  <div class="foot-col" style="left:589px">
    <h4>CONTACT US</h4>
    <ul class="contact-list">
      <li><svg width="14" height="14" viewBox="0 0 18 18" style="margin-top:7px"><path d="M3 2h4l2 4-2 2c1 2 3 4 5 5l2-2 4 2v4c-8 0-15-7-15-15z" fill="#1d1d2b"/></svg>+1 555 014 2297</li>
      <li><svg width="12" height="16" viewBox="0 0 12 16" style="margin-top:6px"><path d="M6 0a6 6 0 0 0-6 6c0 4 6 10 6 10s6-6 6-10a6 6 0 0 0-6-6zm0 8a2 2 0 1 1 0-4 2 2 0 0 1 0 4z" fill="#1d1d2b"/></svg><span>Lorem Ipsum is simply<br>dummy text of the printing</span></li>
      <li><svg width="14" height="14" viewBox="0 0 14 14" style="margin-top:7px"><circle cx="7" cy="7" r="6" fill="none" stroke="#1d1d2b" stroke-width="1.5"/><path d="M7 3v4h3" stroke="#1d1d2b" stroke-width="1.5" fill="none"/></svg>Mon - Fri &nbsp;8AM - 5PM</li>
    </ul>
  </div>
  <div class="foot-col" style="left:880px;width:220px">
    <h4>SIGN UP TO OUR<br>NEWSLETTER</h4>
    <p class="news-note">We Will Notify You Of Any<br>Important News</p>
    <div class="news-input">Your Email Address<b><svg width="22" height="22" viewBox="0 0 22 22" fill="none" stroke="#fff" stroke-width="1.6"><path d="M2 10 20 2l-6 18-4-8z M10 12l10-10"/></svg></b></div>
  </div>
  <div class="foot-rule"></div>
  <p class="copyright">© 2024 Velmo I All Rights Reserved</p>
</footer>

</body>
</html>
```